Hair salon and Nail salon in Hawaii need a newspaper Ad design.

We need a newspaper Ad design for new open hair & nail salon in Waikiki Hawaii.Our Recommendation service for hair is "Head Spa" $30+tax and for nail is "Manicure Treatment Course" (Filing+Cuticle Care+Massage+Coloring) $20+tax.
We would like to see Hawaiian taste color and also having sense of luxury design. The ad size is W 5.0” x H 6.375”.
I would customers to know the shop place(Lanakila Crest Hotel 1F) , phone(808-555-0173), instagram(salonbrightwave) , our web site https://salonbrightwave.example and recommend services. For Web or Instagram , QR code is acceptable.

Target Market(s)

women & men

Industry/Entity Type

Beauty Salon

Font styles to use
Serif

Colors

Designer to choose colors to be used in the design.

Requirements
Must have
• Tagline for local customers. Shop Name is "SALON BRIGHTWAVE".the shop place(Lanakila Crest Hotel 1F) , phone(808-555-0173), instagram(salonbrightwave) and recommend services.
Nice to have
• Our services are competitive, but we don't want to be seen as just cheap and low quality.

```html
<!DOCTYPE html>
<html lang="en">
<head>
<meta charset="utf-8">
<title>Salon Brightwave – Newspaper Ad</title>
<link rel="stylesheet" href="https://fonts.googleapis.com/css2?family=Playfair+Display:wght@700;800&family=Lora:ital,wght@0,400;0,500;0,600;1,400&display=swap">
<style>
  :root {
    --stage: #262f31;
    --mint-light: #d3e6cc;
    --mint: #bcd6b4;
    --mint-deep: #a8c6a2;
    --leaf: rgba(210, 238, 214, 0.85);
    --mauve: rgba(188, 170, 176, 0.9);
    --ink: #111111;
    --paper: #ffffff;
    --hair: #8a5a3e;
    --skin: #d9a88c;
  }
  * { margin: 0; padding: 0; box-sizing: border-box; }
  html, body { width: 1200px; height: 1200px; overflow: hidden; }
  body { background: var(--stage); position: relative; }

  .ad {
    position: absolute;
    left: 161px; top: 40px;
    width: 878px; height: 1120px;
    overflow: hidden;
    color: var(--ink);
  }
  .ad-backdrop {
    position: absolute; inset: 0;
    background: linear-gradient(140deg, var(--mint-light), var(--mint) 55%, var(--mint-deep));
  }
  .ad-portrait {
    position: absolute; left: 430px; top: 0; width: 448px; height: 1120px;
    background:
      radial-gradient(ellipse 150px 200px at 260px 330px, var(--skin), transparent 72%),
      radial-gradient(ellipse 240px 330px at 250px 280px, rgba(138, 90, 62, 0.75), transparent 75%),
      radial-gradient(ellipse 230px 260px at 280px 760px, rgba(217, 168, 140, 0.7), transparent 75%),
      radial-gradient(ellipse 200px 80px at 280px 1080px, rgba(30, 30, 34, 0.7), transparent 75%);
  }
  .ad-shapes { position: absolute; inset: 0; }

  .brand {
    position: absolute; left: 276px; top: 206px;
    font-family: "Playfair Display", serif; font-weight: 800;
    font-size: 32px; letter-spacing: 0;
  }

  .headline {
    position: absolute; left: 52px;
    font-family: "Playfair Display", serif; font-weight: 700; line-height: 1;
  }
  .headline-opening { top: 392px; font-size: 62px; font-weight: 800; letter-spacing: 0.5px; }
  .headline-salon { top: 466px; font-size: 42px; }
  .headline-place { top: 516px; font-size: 42px; }

  .tagline {
    position: absolute; left: 52px; top: 576px;
    font-family: "Lora", serif; font-style: italic; font-size: 23px; line-height: 1;
  }

  .offer {
    position: absolute; left: 52px;
    font-family: "Lora", serif; font-weight: 500; line-height: 1;
  }
  .offer-headspa { top: 624px; display: flex; align-items: center; font-size: 42px; }
  .price-tag {
    display: inline-block; background: var(--paper);
    padding: 8px 18px 9px 10px; margin-left: 10px;
  }
  .offer-manicure { top: 704px; font-size: 34px; }
  .offer-steps { top: 750px; font-size: 22px; font-weight: 400; }
  .offer-price-nail {
    top: 788px; left: 50px; width: 190px;
    background: var(--paper); font-size: 36px; padding: 8px 0 9px 14px;
  }

  .contact {
    position: absolute; left: 52px;
    display: flex; align-items: center; gap: 12px;
    font-family: "Lora", serif; font-weight: 600; font-size: 23px; line-height: 1;
  }
  .contact svg { width: 26px; height: 26px; flex: none; }
  .contact-address { top: 878px; }
  .contact-phone { top: 916px; }
  .contact-social { top: 954px; }
  .contact-web { top: 992px; }
</style>
</head>
<body>
  <main class="ad">
    <div class="ad-backdrop"></div>
    <div class="ad-portrait" role="img" aria-label="Portrait photograph of a woman with long glossy brown hair on a soft mint background"></div>

    <svg class="ad-shapes" viewBox="0 0 878 1120" aria-hidden="true">
      <path fill="var(--leaf)" d="M240 340 C 228 200 290 70 420 50 C 540 32 600 130 590 220 C 578 310 510 344 420 342 Z"/>
      <circle cx="320" cy="810" r="500" fill="var(--mauve)"/>
    </svg>

    <div class="brand">Salonbrightwave</div>

    <h1 class="headline headline-opening">OPENING NEW</h1>
    <p class="headline headline-salon">Hair &amp; Nail salon in</p>
    <p class="headline headline-place">Waikiki Hawaii</p>
    <p class="tagline">Island luxury for hair &amp; nails, close to home</p>

    <p class="offer offer-headspa">Head Spa - <span class="price-tag">$30+Tax</span></p>
    <p class="offer offer-manicure">Manicure Treatment Course</p>
    <p class="offer offer-steps">(Filing+Cuticle Care+Massage+Coloring)</p>
    <p class="offer offer-price-nail">$20+Tax.</p>

    <p class="contact contact-address">
      <svg viewBox="0 0 24 24"><path fill="var(--ink)" d="M12 2a7 7 0 0 0-7 7c0 5 7 13 7 13s7-8 7-13a7 7 0 0 0-7-7zm0 9.5A2.5 2.5 0 1 1 12 6.5a2.5 2.5 0 0 1 0 5z"/></svg>
      Lanakila Crest Hotel 1F
    </p>
    <p class="contact contact-phone">
      <svg viewBox="0 0 24 24"><circle cx="12" cy="12" r="10" fill="none" stroke="var(--ink)" stroke-width="1.6"/><path fill="var(--ink)" d="M9 6.5l1.6 2.6-1 1.2c.6 1.5 1.6 2.6 3.1 3.2l1.2-1 2.6 1.6-.6 1.8c-3.7.2-7.5-3.6-7.4-7.4z"/></svg>
      808-555-0173
    </p>
    <p class="contact contact-social">
      <svg viewBox="0 0 24 24"><circle cx="12" cy="12" r="10" fill="var(--ink)"/></svg>
      salonbrightwave
    </p>
    <p class="contact contact-web">
      <svg viewBox="0 0 24 24"><g fill="none" stroke="var(--ink)" stroke-width="1.6"><circle cx="12" cy="12" r="10"/><ellipse cx="12" cy="12" rx="4" ry="10"/><path d="M2 12h20"/></g></svg>
      salonbrightwave.example
    </p>
  </main>
</body>
</html>
```